Event Planner Looking To Set Apart From Competition

I am a experienced Event/Wedding planner and need to design a unique marketing piece that will be handed out to clients and venues. I would like a postcard, but I am not opposed to another style of printed piece if it's cost effective. I am also looking for a logo that is unique to me and would like to see a few ideas.

Target Market(s)

Brides and Social Event Organizers

Industry/Entity Type

Wedding Planner

Logo Text

Mara Vintelli

Font styles to use
Script

Colors
ffffff
fee3d4
fff3d1
cfeae6
cee9f5
ecdaeb
cedeed

Requirements
Must have
• website reference _ http://www.qrdgatherings.example/planning-packages
• blog reference _ https://blogqrdgatherings.example/meet-mara/
Nice to have
• We can add text once a layout is proposed. If we like the general layout, we will send the text to be included based on the layout.

```html
<!DOCTYPE html>
<html lang="en">
<head>
<meta charset="utf-8">
<title>Burst of Life by QRD Gatherings – Postcard</title>
<link rel="stylesheet" href="https://fonts.googleapis.com/css2?family=Enriqueta:wght@400;600&family=Archivo+Narrow:wght@400;600&display=swap">
<style>
  :root {
    --stage: #f4f1ee;
    --white: #ffffff;
    --peach: #fee3d4;
    --cream: #fff3d1;
    --mint: #cfeae6;
    --sky: #cee9f5;
    --lilac: #ecdaeb;
    --mist: #cedeed;
    --frame-top: #c7a6d3;
    --frame-bottom: #e2bfdc;
    --lilac-edge: #cfaecb;
    --dusk-top: #b9a2c6;
    --dusk-bottom: #8e7299;
    --ink: #2a2030;
    --logo-teal: #4fa9a2;
    --line: #222222;
  }
  * { box-sizing: border-box; margin: 0; padding: 0; }
  html, body { width: 1200px; height: 800px; overflow: hidden; background: var(--stage); }
  .canvas { position: relative; width: 1200px; height: 800px; }

  .postcard {
    position: absolute; top: 78px; width: 414px; height: 644px;
    background: linear-gradient(180deg, var(--frame-top) 0%, var(--frame-bottom) 100%);
    box-shadow: 0 4px 14px rgba(0,0,0,.18);
    overflow: hidden;
  }
  .postcard--front { left: 169px; }
  .postcard--back { left: 618px; }

  .panel {
    position: absolute; left: 13px; right: 13px; top: 13px;
    background: linear-gradient(180deg, var(--lilac) 0%, var(--mist) 45%, var(--lilac) 100%);
  }
  .postcard--front .panel { height: 432px; }
  .postcard--back .panel { bottom: 13px; background: linear-gradient(180deg, var(--mist) 0%, var(--lilac) 55%, var(--peach) 100%); }

  .logo-card {
    position: absolute; left: 110px; width: 204px; height: 124px;
    background: var(--white); border: 5px solid rgba(255,255,255,.6);
    outline: 1px solid rgba(120,120,120,.25);
    display: flex; align-items: center; justify-content: center;
  }
  .logo-name { font-family: "Enriqueta", serif; font-weight: 400; font-size: 22px; color: var(--logo-teal); }

  .serif { font-family: "Enriqueta", serif; font-weight: 400; color: var(--ink); }
  .title { position: absolute; left: 0; right: 0; text-align: center; font-size: 21px; }
  .quote { position: absolute; left: 0; right: 0; top: 204px; text-align: center; font-size: 11px; }
  .meet { position: absolute; left: 60px; top: 222px; font-size: 21px; }

  .photo { position: absolute; background: linear-gradient(160deg, #c9b2bd, #7d6a72); }
  .bio {
    position: absolute; left: 175px; top: 232px; width: 208px;
    font-family: "Archivo Narrow", sans-serif; font-size: 6.4px; line-height: 1.35;
    color: var(--ink); text-align: justify;
  }
  .bio p + p { margin-top: 6px; }

  .address { position: absolute; left: 0; right: 0; top: 454px; bottom: 0; background: var(--white); }
  .references {
    position: absolute; left: 41px; top: 10px; right: 20px;
    font-family: "Archivo Narrow", sans-serif; font-size: 8px; line-height: 1.4; color: var(--ink);
  }
  .address-line { position: absolute; left: 41px; height: 1px; background: var(--line); width: 233px; }
  .stamp-box { position: absolute; left: 305px; top: 45px; width: 77px; height: 72px; border: 1px solid var(--line); }

  .skyline {
    position: absolute; left: 13px; right: 13px; top: 13px; height: 258px;
    background: linear-gradient(180deg, var(--dusk-top) 0%, var(--dusk-bottom) 75%);
    clip-path: polygon(0 0, 100% 0, 100% 72%, 0 100%);
  }
  .ribbons { position: absolute; left: 0; top: 0; }
  .ribbon-shape { fill: var(--lilac); stroke: var(--lilac-edge); stroke-width: 1; }
  .ribbon-text { font-family: "Enriqueta", serif; font-size: 12px; fill: var(--ink); }

  .lead { position: absolute; left: 0; right: 0; top: 300px; text-align: center; font-size: 12.5px; }
  .heading { position: absolute; left: 0; right: 0; top: 322px; text-align: center; font-size: 22px; }

  .gallery {
    position: absolute; left: 28px; top: 362px; width: 358px; height: 126px;
    display: grid; grid-template-columns: repeat(4, 1fr); grid-template-rows: repeat(2, 1fr);
  }
  .gallery .tile:nth-child(1) { background: linear-gradient(135deg, var(--peach), #d9a994); }
  .gallery .tile:nth-child(2) { background: linear-gradient(135deg, var(--white), #cbbfb6); }
  .gallery .tile:nth-child(3) { background: linear-gradient(135deg, var(--lilac), #b49ccc); }
  .gallery .tile:nth-child(4) { background: linear-gradient(135deg, #e4e4e4, #9c9c9c); }
  .gallery .tile:nth-child(5) { background: linear-gradient(135deg, var(--cream), #c9a97e); }
  .gallery .tile:nth-child(6) { background: linear-gradient(135deg, var(--peach), #b99272); }
  .gallery .tile:nth-child(7) { background: linear-gradient(135deg, var(--sky), #9fb8c4); }
  .gallery .tile:nth-child(8) { background: linear-gradient(135deg, var(--cream), #e0cdb5); }

  .link-button {
    position: absolute; width: 112px; height: 31px;
    background: var(--lilac); border: 1px solid var(--lilac-edge);
    display: flex; align-items: center; justify-content: center;
    font-family: "Archivo Narrow", sans-serif; font-weight: 600; font-size: 10px; color: var(--ink);
  }
  .link-button::before, .link-button::after {
    content: ""; position: absolute; width: 4px; height: 4px; border-radius: 50%;
    background: rgba(255,255,255,.8); left: 4px; top: 4px;
  }
  .link-button::after { left: auto; right: 4px; top: auto; bottom: 4px; }
  .lighting { position: absolute; left: 52px; top: 593px; font-size: 18px; }
</style>
</head>
<body>
<main class="canvas">

  <section class="postcard postcard--front">
    <div class="panel" role="img" aria-label="Soft-focus photo of a candlelit reception table in pastel tones"></div>
    <div class="logo-card" style="top:37px"><span class="logo-name">QRD Gatherings</span></div>
    <h1 class="serif title" style="top:176px">Burst of Life by QRD Gatherings</h1>
    <p class="serif quote">"I need a burst of life. That's entertainment for me". – Dana Roux</p>
    <h2 class="serif meet">Meet Mara:</h2>
    <div class="photo" style="left:33px;top:254px;width:128px;height:171px" role="img" aria-label="Photo of Mara helping a bride in a lace gown get ready"></div>
    <div class="bio">
      <p>Mara Vintelli moved to Atlanta in 2007 to become part of the opening sales team for the prestigious Harlow Civic Arts Centre where she worked with in-demand artists and planned some of Atlanta's most exclusive galas, fundraisers and celebrations.</p>
      <p>Mara later became part of Jonah Pell's Signature Events team and A Gilded Affair working as a sales consultant arranging catering menus, event floral and complete event design.</p>
      <p>Mara's "behind-the-scenes" expertise in these areas of venue management, catering, floral and design consulting for some of Atlanta's best event companies allows her to provide clients with a unique perspective and a very special planning experience.</p>
      <p>An active member of Atlanta's professional events community, Mara was honored with the Rowan Ellis Rising Star Award in 2011. This Lumen Award is presented annually by the Atlanta chapters of IGEP (International Guild of Event Professionals) and NCEA (National Council of Event Associates). Mara has been a contributing member of the Lumen Awards steering committee since 2008, serving as venue liaison, logistics chairperson, food and beverage chairperson and on the marketing and public relations committee.</p>
    </div>
    <div class="address">
      <p class="references">Planning packages: http://www.qrdgatherings.example/planning-packages<br>Meet Mara: https://blogqrdgatherings.example/meet-mara/</p>
      <span class="address-line" style="top:45px"></span>
      <span class="address-line" style="top:82px"></span>
      <span class="address-line" style="top:118px"></span>
      <span class="address-line" style="top:154px;width:341px"></span>
      <span class="stamp-box"></span>
    </div>
  </section>

  <section class="postcard postcard--back">
    <div class="panel" role="img" aria-label="Soft-focus photo of reception flowers and candles in pastel pink and lilac"></div>
    <div class="skyline" role="img" aria-label="City skyline silhouette at dusk"></div>
    <div class="logo-card" style="top:53px"><span class="logo-name">QRD Gatherings</span></div>
    <svg class="ribbons" width="414" height="300" viewBox="0 0 414 300">
      <g transform="translate(62,250) rotate(-15)">
        <polygon class="ribbon-shape" points="0,0 128,0 122,11 128,22 0,22 6,11"/>
        <text class="ribbon-text" x="64" y="15.5" text-anchor="middle">Congratulations!</text>
      </g>
      <g transform="translate(178,262) rotate(-15)">
        <polygon class="ribbon-shape" points="0,0 128,0 122,11 128,22 0,22 6,11"/>
        <text class="ribbon-text" x="64" y="15.5" text-anchor="middle">Congratulations!</text>
      </g>
      <g transform="translate(274,278) rotate(-15)">
        <polygon class="ribbon-shape" points="0,0 128,0 122,11 128,22 0,22 6,11"/>
        <text class="ribbon-text" x="64" y="15.5" text-anchor="middle">Congratulations!</text>
      </g>
    </svg>
    <p class="serif lead">You're engaged, and it's time for the wedding planning to begin.</p>
    <h2 class="serif heading">Full Planning &amp; Coordination</h2>
    <div class="gallery">
      <div class="tile" role="img" aria-label="Portrait of a smiling bride"></div>
      <div class="tile" role="img" aria-label="Couple cutting a tiered wedding cake"></div>
      <div class="tile" role="img" aria-label="Ballroom lit in purple with couple dancing"></div>
      <div class="tile" role="img" aria-label="Black and white photo of guests dancing"></div>
      <div class="tile" role="img" aria-label="Grand ballroom with chandeliers"></div>
      <div class="tile" role="img" aria-label="Church ceremony interior"></div>
      <div class="tile" role="img" aria-label="Flower girls in white dresses"></div>
      <div class="tile" role="img" aria-label="Decorated reception chairs"></div>
    </div>
    <span class="link-button" style="left:28px;top:508px">Ceremony Music</span>
    <span class="link-button" style="left:151px;top:508px">Father Daughter Dance</span>
    <span class="link-button" style="left:274px;top:508px">Processional</span>
    <span class="link-button" style="left:28px;top:549px">Mother Son Dance</span>
    <span class="link-button" style="left:151px;top:549px">Recessional</span>
    <span class="link-button" style="left:274px;top:549px">Cake Cutting</span>
    <h3 class="serif lighting">Custom Wedding Lighting</h3>
    <span class="link-button" style="left:274px;top:589px">Wedding Gobo Catalog</span>
  </section>

</main>
</body>
</html>
```